Minimalist Professional Business Card Design

We will be revamping our marketing materials: Business cards, Website and Catalogs.
Our Overall Design direction is to have a Minimalist artwork with Professionalism and Premium feel. The revamp starts with the new business card design followed by the others. Thus the designer whom work is selected for this job will likely to follow through with the subsequent jobs.

Target Market(s)

Upscale

Industry/Entity Type

Manufacturing

Contact Information for Business Card

For the Business Cards, the following are required:
. Minimalist yet Professional and Premium Feel
. Background Colors: white and / or light pastel yellow and if needed to smoothen the yellow, the light grey can be incorporated. We are changing our corporate bright yellow to either one of the three alternatives:
1. Soylant yellow CMYK (1%, 0%, 52%, 3%)
2. Popcorn yellow CMYK (0%, 0%, 33%, 0%)
3. Papaya yellow CMYK (0%, 0%, 51%, 0%)

Information to be inputed in the business cards:

Name: Barlen Moritova
Position: Managing Director

Company's name: Vellomar Valves Pte. Ltd.
Address: 512 Halvick Lane #07-09B
Singapore 617302
Tel: (65) 6281 4096
Fax: (65) 6294 7118
Email: barlen@vellomarvalves-example.com
Website: www.vellomarvalves-example.com
Skype: Vellomar.Valves
Whatsapp/ Line/ Viber/ WeChat: (65) 9372 6081

Company's Logo
Company's Slogan
Two product photos placed side by side (if this gets into the way of the design, it is OK not to include them)

Font styles to use
Serif

Colors
ffffff

Requirements
Must have
• Minimalist
Should not have
• Messy, crowded, playful

```html
<!DOCTYPE html>
<html lang="en">
<head>
<meta charset="utf-8">
<title>Vellomar Valves – Business Card</title>
<link rel="stylesheet" href="https://fonts.googleapis.com/css2?family=Roboto+Slab:wght@300;700&family=Roboto:wght@400&display=swap">
<style>
  :root {
    --backdrop: #262626;
    --card-dark: #1c1c1c;
    --card-light: #f4f4f4;
    --ink-dark: #3a3a3a;
    --ink-mid: #6a6a6a;
    --disc: #707070;
    --disc-tab: #555555;
    --logo-grey: #5d5d5d;
    --white: #ffffff;
  }
  * { margin: 0; padding: 0; box-sizing: border-box; }
  html, body { width: 1200px; height: 886px; overflow: hidden; background: var(--backdrop); }
  .stage { position: relative; width: 1200px; height: 886px; }
  .card {
    position: absolute; left: 270px; width: 660px; height: 377px;
    border-radius: 22px; overflow: hidden;
  }
  /* back */
  .card-back { top: 45px; background: var(--card-dark); }
  .product-photo {
    position: absolute; top: 30px; width: 90px; height: 317px; border-radius: 8px;
    background: linear-gradient(90deg, #8d8d8d, #e6e6e6 45%, #9a9a9a);
  }
  .product-photo.left { left: 40px; }
  .product-photo.right { right: 40px; }
  .brand-block { position: absolute; left: 150px; right: 150px; top: 90px; text-align: center; }
  .brand-mark { width: 90px; height: 90px; border-radius: 50%; background: var(--logo-grey); margin: 0 auto 14px; }
  .brand-name-back {
    font-family: "Roboto Slab", serif; font-weight: 700; font-size: 54px;
    color: var(--logo-grey); letter-spacing: 1px; line-height: 1;
  }
  .slogan {
    font-family: "Roboto", sans-serif; font-size: 13px; color: var(--logo-grey);
    letter-spacing: 1px; margin-top: 8px; white-space: nowrap;
  }
  /* front */
  .card-front { top: 464px; background: var(--card-light); }
  .name-disc {
    position: absolute; left: 30px; top: 35px; width: 290px; height: 290px;
    border-radius: 50%; background: var(--disc);
  }
  .disc-tab { position: absolute; left: 318px; top: 185px; width: 22px; height: 40px; background: var(--disc-tab); }
  .person {
    position: absolute; left: 30px; top: 155px; width: 290px; text-align: center; color: var(--white);
    font-family: "Roboto Slab", serif;
  }
  .person-name { font-weight: 700; font-size: 22px; letter-spacing: 1px; }
  .person-title { font-weight: 300; font-size: 14px; letter-spacing: 1.5px; margin-top: 2px; }
  .brand-name-front {
    position: absolute; right: 40px; top: 40px;
    font-family: "Roboto Slab", serif; font-weight: 700; font-size: 44px; color: var(--ink-dark);
  }
  .contact {
    position: absolute; right: 40px; top: 130px; text-align: right;
    font-family: "Roboto", sans-serif; font-size: 14px; line-height: 20px; color: var(--ink-dark);
  }
  .contact .gap { height: 8px; }
  .row { display: flex; justify-content: flex-end; align-items: center; gap: 6px; white-space: nowrap; }
  .row svg { width: 13px; height: 13px; fill: var(--ink-mid); flex: none; }
  .row .fax { display: flex; align-items: center; gap: 5px; margin-right: 8px; }
</style>
</head>
<body>
<div class="stage">

  <section class="card card-back">
    <div class="product-photo left" role="img" aria-label="Product photo: stainless steel submersible pump"></div>
    <div class="brand-block">
      <div class="brand-mark"></div>
      <div class="brand-name-back">VELLOMAR</div>
      <div class="slogan">BUILT WITH CARE I MADE TO ENDURE</div>
    </div>
    <div class="product-photo right" role="img" aria-label="Product photo: stainless steel pump motor"></div>
  </section>

  <section class="card card-front">
    <div class="name-disc"></div>
    <div class="disc-tab"></div>
    <div class="person">
      <div class="person-name">BARLEN MORITOVA</div>
      <div class="person-title">MANAGING DIRECTOR</div>
    </div>

    <div class="brand-name-front">VELLOMAR</div>

    <div class="contact">
      <div>Vellomar Valves Pte. Ltd.</div>
      <div>512 Halvick Lane #07-09B</div>
      <div>Singapore 617302</div>
      <div class="gap"></div>
      <div class="row">
        <span class="fax"><span>(65) 6294 7118</span>
          <svg viewBox="0 0 16 16"><rect x="4" y="1" width="8" height="5"/><rect x="1" y="6" width="14" height="6" rx="1"/><rect x="4" y="10" width="8" height="5"/></svg></span>
        <span>(65) 6281 4096</span>
        <svg viewBox="0 0 16 16"><path d="M3 1l3 3-2 2c1 2 3 4 6 6l2-2 3 3-2 2C7 15 1 9 1 3z"/></svg></div>
      <div class="row"><span>(65) 9372 6081</span>
        <svg viewBox="0 0 16 16"><circle cx="8" cy="8" r="7"/></svg></div>
      <div class="row"><span>barlen@vellomarvalves-example.com</span>
        <svg viewBox="0 0 16 16"><path d="M1 3h14v10H1z M1 3l7 6 7-6" fill="none" stroke="#6a6a6a" stroke-width="1.6"/></svg></div>
      <div class="row"><span>Vellomar.Valves</span>
        <svg viewBox="0 0 16 16"><circle cx="8" cy="8" r="7"/></svg></div>
    </div>
  </section>

</div>
</body>
</html>
```